A website design for a consultation firm

We are located in Istanbul, Turkey and offers our consultation services to customers interested in investing in Realestate, Education and Investment particularly this coming from Arab world and English speaking countries.

The site should carry our message of deep knowledge about the Turkish markets in the mentioned sectors of interest, sincerity and keenness.

The final deliverable of the winning design should include:
- The source files of the final designs. e.g. AI, PSD ..etc
- The redline markup for the design using a Specctr or any other similar tool.

Target Market(s)

English and Arabic speaking countries with a Turkish theme since we are a Turkish company

Industry/Entity Type

Consulting

Number of Pages Required

2 page

Font styles to use
Sans Serif

Requirements
Must have
• The site should serve the following main sections:
• - Why QVE?
• - Reports & studies
• - Sectors
• - Our team
• - Contact
• We need a design that could be converted into a WordPress theme.
• The design should be in English but should accommodate other languages including RTL.
• You can use the color theme you like as long as it does't dissolve the logo.
• The site should link into our accounts on the following networks:
• - Twitter
• - Facebook
• - LinkedIn
• The design should be responsive and nicely rendered on Desktop, Tablets and Smart phones.
Nice to have
• The site would be nice to balance between being informative and

```html
<!DOCTYPE html>
<html lang="en">
<head>
<meta charset="utf-8">
<title>QVE Consulting</title>
<link rel="stylesheet" href="https://fonts.googleapis.com/css2?family=Roboto:wght@400;500;700;900&family=Questrial&display=swap">
<style>
:root{
  --navy:#1f3a6b;
  --navy-dark:#172d55;
  --red:#e51b2a;
  --ink:#2b2b2b;
  --muted:#5c5c5c;
  --light:#f3f3f3;
  --line:#e2e2e2;
  --white:#ffffff;
}
*{box-sizing:border-box;margin:0;padding:0}
html,body{width:1200px;height:2839px;overflow:hidden}
body{font-family:'Roboto',sans-serif;color:var(--ink);background:var(--white);position:relative}
.abs{position:absolute}
p{line-height:1.45}
a{text-decoration:none}

/* header */
.topbar{left:0;top:0;width:1200px;height:34px;background:#eeeff2}
.topbar .contact{top:9px;font-size:12px;color:var(--muted);display:flex;align-items:center;gap:8px}
.search{left:852px;top:3px;width:218px;height:28px;background:var(--white);border:1px solid var(--line);font-size:12px;color:var(--muted);padding:7px 10px}
.search svg{position:absolute;right:10px;top:7px}
.mainnav{left:0;top:34px;width:1200px;height:64px;background:var(--white);border-bottom:1px solid var(--line)}
.mainnav a{position:absolute;top:25px;font-size:14px;color:var(--ink)}
.brand-tab{left:537px;top:0;width:128px;height:86px;background:var(--white);border:1px solid var(--line);border-top:none;display:flex;align-items:center;justify-content:center;gap:6px}
.brand{font-weight:900;color:var(--red);font-size:30px;letter-spacing:1px}
.brand-dot{width:12px;height:12px;border-radius:50%;background:var(--navy)}

/* hero */
.hero{left:0;top:98px;width:1200px;height:489px;background:linear-gradient(90deg,#eef1f3 0%,#dfe6ea 35%,#9fb0be 60%,#7f8f9d 100%)}
.hero .welcome{left:129px;top:168px;font-size:22px;color:var(--navy)}
.hero h1{left:127px;top:190px;font-size:50px;font-weight:700;color:var(--navy);letter-spacing:1px}
.hero .lead{left:129px;top:252px;width:310px;font-size:13px;color:#333}
.btn{display:inline-flex;align-items:center;justify-content:center;border-radius:17px;color:var(--white);font-size:12px;font-weight:500;height:34px}
.hero .btn{left:129px;top:326px;width:100px;background:var(--navy)}
.dots{display:flex;gap:5px}
.dots i{width:8px;height:8px;border-radius:50%;background:var(--navy)}
.dots i.on{background:var(--red)}

/* why */
.why{left:0;top:587px;width:1200px;height:479px;background:var(--light)}
.section-title{width:1200px;text-align:center;font-weight:700}
.why .section-title{top:62px;font-size:34px;color:var(--navy);letter-spacing:3px}
.sub{width:1200px;text-align:center;font-size:13px;color:var(--muted)}
.why .sub{top:114px}
.feature{top:212px;width:300px;height:189px;background:var(--white);text-align:center}
.feature .icon{position:absolute;left:103px;top:-47px;width:94px;height:94px;border-radius:50%;background:var(--white);box-shadow:0 2px 6px rgba(0,0,0,.12);display:flex;align-items:center;justify-content:center}
.feature .icon.active{background:var(--navy)}
.feature h3{margin-top:63px;font-size:17px;font-weight:500;color:var(--navy)}
.feature p{margin:10px auto 0;width:230px;font-size:13px;color:var(--muted)}
.feature .more{display:block;margin-top:8px;font-size:12px;font-weight:500;color:var(--ink)}

/* reports */
.reports{left:0;top:1066px;width:1200px;height:477px;background:var(--white)}
.rs-title{top:130px;font-size:33px;font-weight:700}
.rs-sub{top:183px;font-size:15px;font-weight:700;color:var(--ink)}
.rs-text{top:212px;width:350px;font-size:13px;color:var(--muted)}
.amp{left:590px;top:225px;font-size:22px;color:var(--ink)}

/* sectors */
.sectors{left:0;top:1543px;width:1200px;height:554px;background:linear-gradient(180deg,#2a4677 0%,#1f3a6b 55%,#243f70 100%)}
.sectors .section-title{top:58px;font-family:'Questrial',sans-serif;font-size:48px;color:var(--white)}
.sectors .sub{top:118px;color:var(--white);font-size:13px}
.sector-card{top:191px;width:388px;height:210px;background:var(--white);padding:28px 32px}
.sector-card h3{font-size:18px;font-weight:500;color:var(--ink);line-height:1.3;width:260px}
.sector-card p{margin-top:10px;font-size:13px;color:var(--muted)}
.sector-card .more{display:block;margin-top:10px;font-size:12px;color:var(--ink)}
.sectors .dots{left:582px;top:450px}
.sectors .dots i{background:#9aa7bd}
.sectors .dots i.on{background:var(--white)}

/* team */
.team{left:0;top:2097px;width:1200px;height:614px;background:linear-gradient(180deg,#f0f0f0 0%,#f7f7f7 45%,#fafafa 100%)}
.team .section-title{top:66px;font-family:'Questrial',sans-serif;font-weight:400;font-size:34px;color:var(--ink)}
.team .sub{top:118px}
.team-photo{left:0;top:230px;width:1200px;height:384px;background:linear-gradient(180deg,rgba(230,230,230,0) 0%,#d8cfc8 40%,#8e8a8c 100%)}
.pin{width:30px;height:30px;border-radius:50%;background:var(--red);color:var(--white);font-size:20px;line-height:27px;text-align:center;font-weight:500;border:2px solid var(--white)}
.popup{left:733px;top:212px;width:246px;height:133px;background:var(--red);color:var(--white);padding:20px 18px}
.popup h4{font-size:14px;font-weight:700}
.popup p{margin-top:6px;font-size:12px;line-height:1.35}
.popup .more{display:block;margin-top:10px;font-size:11px;color:var(--white)}

/* footer */
.footer{left:0;top:2711px;width:1200px;height:128px;background:var(--navy)}
.footer .wedge{left:0;top:0}
.footer .foot-brand{left:128px;top:40px;display:flex;align-items:center;gap:6px}
.footer nav a{position:absolute;top:30px;font-size:13px;color:var(--white)}
.copy{right:130px;top:68px;font-size:11px;color:#c8d0de}
.social{right:130px;top:92px;display:flex;gap:14px}
.social i{width:10px;height:10px;border-radius:50%;background:var(--white);display:block}
</style>
</head>
<body>

<header>
  <div class="abs topbar">
    <div class="abs contact" style="left:129px">
      <svg width="10" height="14" viewBox="0 0 10 14"><rect x="1" y="0.5" width="8" height="13" rx="1.5" fill="none" stroke="#444"/><circle cx="5" cy="11" r="0.9" fill="#444"/></svg>
      555-010-0199
    </div>
    <div class="abs" style="left:229px;top:8px;width:1px;height:18px;background:#ccc"></div>
    <div class="abs contact" style="left:246px">
      <svg width="14" height="10" viewBox="0 0 14 10"><rect x="0.5" y="0.5" width="13" height="9" fill="#444"/><path d="M1 1 L7 6 L13 1" stroke="#eee" fill="none"/></svg>
      info@qve
    </div>
    <div class="abs search">Search Here
      <svg width="14" height="14" viewBox="0 0 14 14"><circle cx="6" cy="6" r="4.5" fill="none" stroke="#333" stroke-width="1.6"/><path d="M9.5 9.5 L13 13" stroke="#333" stroke-width="1.8"/></svg>
    </div>
  </div>
  <nav class="abs mainnav">
    <a href="#" style="left:125px">Home</a>
    <a href="#" style="left:212px">Why QVE?</a>
    <a href="#" style="left:324px">Reports &amp; studies</a>
    <a href="#" style="left:791px">Sectors</a>
    <a href="#" style="left:890px">Our Team</a>
    <a href="#" style="left:1001px">Contact Us</a>
  </nav>
  <div class="abs brand-tab"><span class="brand">QVE</span><span class="brand-dot"></span></div>
</header>

<section class="abs hero" role="img" aria-label="Three business people in a meeting around a table in a bright glass office">
  <div class="abs welcome">Welcome to</div>
  <h1 class="abs">Consulting</h1>
  <p class="abs lead">There are many variations of passages of Lorem Ipsum available, but the majority have suffered alteration in some form,</p>
  <a class="abs btn" href="#">Read More</a>
  <div class="abs dots" style="left:129px;top:438px"><i></i><i class="on"></i><i></i><i></i></div>
</section>

<section class="abs why">
  <h2 class="abs section-title">Why QVE?</h2>
  <p class="abs sub">Lorem Ipsum available, but the majority suffered alteration<br>in some form, by injected humour or randomised.</p>

  <article class="abs feature" style="left:127px">
    <div class="icon"><svg width="30" height="30" viewBox="0 0 30 30" fill="none" stroke="#888" stroke-width="1.2"><rect x="6" y="4" width="18" height="23"/><path d="M10 9h3M17 9h3M10 14h3M17 14h3M10 19h3M17 19h3M13 27v-4h4v4"/></svg></div>
    <h3>Realestate</h3>
    <p>There are many variations of pas sag es of Lorem Ipsum available,</p>
    <a class="more" href="#">Read More &nbsp;›</a>
  </article>
  <article class="abs feature" style="left:451px">
    <div class="icon active"><svg width="30" height="30" viewBox="0 0 30 30" fill="none" stroke="#fff" stroke-width="1.3"><rect x="8" y="4" width="14" height="20"/><path d="M11 9h8M11 13h8M13 24l2 4 2-4"/></svg></div>
    <h3>Education</h3>
    <p>There are many variations of pas sag es of Lorem Ipsum available,</p>
    <a class="more" href="#" style="color:var(--navy)">Read More &nbsp;›</a>
  </article>
  <article class="abs feature" style="left:769px">
    <div class="icon"><svg width="30" height="30" viewBox="0 0 30 30" fill="none" stroke="#888" stroke-width="1.2"><path d="M6 22c0-9 4-15 10-15s8 5 6 9l-3 2v4h-5"/><path d="M24 11c2 2 2 5 0 7M27 9c3 3 3 8 0 11"/></svg></div>
    <h3>English speaking countries</h3>
    <p>There are many variations of pas sag es of Lorem Ipsum available,</p>
    <a class="more" href="#">Read More &nbsp;›</a>
  </article>
</section>

<section class="abs reports">
  <svg class="abs" style="left:380px;top:80px" width="440" height="360" viewBox="0 0 440 360">
    <defs>
      <radialGradient id="glow" cx="50%" cy="50%" r="50%">
        <stop offset="0" stop-color="#bfe4ef" stop-opacity=".7"/>
        <stop offset="1" stop-color="#ffffff" stop-opacity="0"/>
      </radialGradient>
    </defs>
    <ellipse cx="220" cy="180" rx="200" ry="160" fill="url(#glow)"/>
    <path d="M20 20 L420 340 M420 20 L20 340" stroke="#cfe3ea" stroke-width="1"/>
  </svg>
  <div class="abs" style="left:552px;top:112px;width:96px;height:46px;background:var(--white);display:flex;align-items:center;justify-content:center;gap:6px"><span class="brand">QVE</span><span class="brand-dot"></span></div>
  <div class="abs amp">&amp;</div>

  <h2 class="abs rs-title" style="left:125px;color:var(--red)">Reports</h2>
  <h3 class="abs rs-sub" style="left:127px">Lorem Ipsum available</h3>
  <p class="abs rs-text" style="left:127px">There are many variations of pas sag es of Lorem Ipsum available, but the majority suffered alterationin some form by injected humour, or randomised words which don't look even slightly believable.</p>
  <a class="abs btn" href="#" style="left:127px;top:314px;width:110px;background:var(--red)">Read More &nbsp;›</a>

  <h2 class="abs rs-title" style="right:130px;color:var(--navy)">Studies</h2>
  <h3 class="abs rs-sub" style="right:130px">Contrary to popular belief</h3>
  <p class="abs rs-text" style="right:130px;text-align:right">Lorem Ipsum is not simply random text. It has roots in a piece of classical Latin literature from 45 BC, making it over 2000 years old. Elena Varga, a Latin professor at Northfield Hall College in Vermont,</p>
  <a class="abs btn" href="#" style="left:962px;top:314px;width:108px;background:var(--navy)">Read More &nbsp;›</a>
</section>

<section class="abs sectors" role="img" aria-label="Busy city street crowd behind a deep blue overlay">
  <h2 class="abs section-title">Sectors</h2>
  <p class="abs sub">There are many variations of pas sag es of Lorem Ipsum available, but<br>the majority suffered alterationin some.</p>
  <article class="abs sector-card" style="left:204px">
    <h3>Lorem Ipsum available avaliable but the majority</h3>
    <p>There are many variations of pas sag es of Lorem Ipsum available, but the majority suffered alterationin some form by injected humour, or randomised words which don't look even slightly believable.</p>
    <a class="more" href="#">Read More →</a>
  </article>
  <article class="abs sector-card" style="left:608px">
    <h3>Lorem Ipsum available avaliable but the majority</h3>
    <p>There are many variations of pas sag es of Lorem Ipsum available, but the majority suffered alterationin some form by injected humour, or randomised words which don't look even slightly believable.</p>
    <a class="more" href="#">Read More →</a>
  </article>
  <div class="abs dots"><i class="on"></i><i></i><i class="on"></i></div>
</section>

<section class="abs team">
  <h2 class="abs section-title">Our team</h2>
  <p class="abs sub">There are many variations of pas sag es of Lorem Ipsum available,<br>but the majority suffered alterationin some.</p>
  <div class="abs team-photo" role="img" aria-label="Row of team members holding tablets, phones and laptops"></div>
  <div class="abs popup">
    <h4>Lorem Ipsum Available</h4>
    <p>There are many variations of pas sag es of Lorem Ipsum available.</p>
    <a class="more" href="#">Read More →</a>
  </div>
  <svg class="abs" style="left:733px;top:344px" width="20" height="20" viewBox="0 0 20 20"><path d="M0 0 H20 L0 20 Z" fill="#e51b2a"/></svg>
  <div class="abs pin" style="left:216px;top:288px">+</div>
  <div class="abs pin" style="left:32px;top:358px">+</div>
  <div class="abs pin" style="left:396px;top:444px">+</div>
  <div class="abs pin" style="left:545px;top:457px">+</div>
  <div class="abs pin" style="left:716px;top:362px">-</div>
  <div class="abs pin" style="left:790px;top:455px">+</div>
  <div class="abs pin" style="left:952px;top:383px">+</div>
  <div class="abs pin" style="left:1121px;top:434px">+</div>
</section>

<footer class="abs footer">
  <svg class="abs wedge" width="350" height="128" viewBox="0 0 350 128"><path d="M0 0 H272 L348 64 L272 128 H0 Z" fill="#fff"/></svg>
  <div class="abs foot-brand"><span class="brand" style="font-size:34px">QVE</span><span class="brand-dot"></span></div>
  <nav>
    <a href="#" style="left:602px">Home</a>
    <a href="#" style="left:664px">Why QVE?</a>
    <a href="#" style="left:748px">Reports &amp; studies</a>
    <a href="#" style="left:873px">Sectors</a>
    <a href="#" style="left:945px">Our team</a>
    <a href="#" style="left:1025px">Contact</a>
  </nav>
  <div class="abs copy">Copyright © 2016 qve-consult.example</div>
  <div class="abs social" aria-label="Social network links"><i></i><i></i><i></i></div>
</footer>

</body>
</html>
```